hawkforge structural steel

8 1/2" x 11" flyer color both sides. Use at least 12 pictures.

Add the word; structural under HawkForge to logo

bullet points:
Laser Accuracy
On-time scheduling
Own our Equipment
39 Years Exp.
Manufacturing Construction Brackets Since 1982
We manufacture custom ibeams in Phoenix, AZ
Certified welders

Hawkforge Plant
2814 n. 17th avenue, suite-3
Phx, AZ 85019
480-629-8107

Target Market(s)

Architects, builders

Industry/Entity Type

construction

Colors
0054AA
0677BA
7BADD7
CADEEF
E8F1F8

```html
<!DOCTYPE html>
<html lang="en">
<head>
<meta charset="utf-8">
<title>HawkForge Structural Flyer</title>
<link rel="stylesheet" href="https://fonts.googleapis.com/css2?family=Poppins:wght@300;400;500;600;700;800&family=Oswald:wght@400;500;600&display=swap">
<style>
  :root {
    --brand-blue: #45669c;
    --brand-blue-dark: #3a5a8c;
    --ink: #2b2b2b;
    --footer-black: #232323;
    --mid-gray: #8e8e8e;
    --paper: #ffffff;
    --soft-bg: #f4f5f7;
    --steel-light: #dfe4ea;
    --steel-mid: #9aa6b4;
  }
  * { margin: 0; padding: 0; box-sizing: border-box; }
  html, body { width: 1200px; height: 2400px; overflow: hidden; }
  body { background: var(--paper); font-family: 'Poppins', sans-serif; position: relative; }

  .flyer {
    position: absolute; left: 50px; top: 488px;
    width: 1016px; height: 1316px;
    transform: scale(1.0827); transform-origin: top left;
    background: var(--soft-bg);
    box-shadow: 0 10px 30px rgba(0,0,0,0.18);
    overflow: hidden;
  }

  .brand-panel {
    position: absolute; left: 0; top: 0; width: 534px; height: 540px;
    background: var(--brand-blue);
  }
  .brand-mark {
    position: absolute; left: 190px; top: 50px; width: 110px; height: 110px;
    border: 5px solid #fff; border-radius: 50%;
  }
  .brand-name {
    position: absolute; left: 44px; top: 186px;
    color: #fff; font-weight: 400; font-size: 50px; line-height: 1; letter-spacing: 1px;
    white-space: nowrap;
  }
  .brand-name span { display: block; font-size: 35px; letter-spacing: 14px; margin-top: 8px; }

  .headline { position: absolute; left: 44px; top: 330px; width: 480px; color: #fff; font-weight: normal; }
  .headline-top { font-size: 66px; line-height: 1; letter-spacing: 1px; white-space: nowrap; }
  .headline-top b { font-weight: 800; }
  .headline-top i { font-style: normal; font-weight: 400; }
  .headline-bottom {
    display: inline-block; white-space: nowrap;
    font-family: 'Oswald', sans-serif; font-weight: 600; font-size: 72px;
    line-height: 1; margin-top: 4px; letter-spacing: -0.5px;
    transform: scaleX(0.86); transform-origin: left center;
  }

  .stock-photo {
    position: absolute; left: 534px; top: 0; width: 482px; height: 540px;
    background: linear-gradient(135deg, #c9d0d9 0%, #8d99a8 50%, #b9c2cd 100%);
  }
  .tube-photo {
    position: absolute; left: 20px; top: 490px; width: 470px; height: 300px;
    background: radial-gradient(ellipse at 60% 55%, #e6e8eb 0%, #b8bcc2 55%, rgba(244,245,247,0) 80%);
  }

  .features { position: absolute; left: 0; top: 790px; width: 620px; height: 410px; }
  .feature { position: absolute; width: 220px; text-align: center; }
  .feature-icon {
    width: 98px; height: 98px; margin: 0 auto; border-radius: 50%;
    background: #fff; border: 3px solid var(--brand-blue);
    box-shadow: 0 0 0 6px #fff, 0 4px 12px rgba(0,0,0,0.25);
    display: flex; align-items: center; justify-content: center;
  }
  .feature-label {
    margin-top: 14px; font-weight: 700; font-size: 19px; line-height: 1.05;
    color: var(--ink); text-transform: uppercase;
  }
  .rule { position: absolute; background: var(--brand-blue); }

  .experience { position: absolute; left: 586px; top: 582px; }
  .experience-years { font-size: 72px; font-weight: 800; color: var(--brand-blue); line-height: 1; letter-spacing: 1px; white-space: nowrap; }
  .experience-word { font-size: 63px; font-weight: 500; color: var(--mid-gray); line-height: 1; margin-top: 2px; letter-spacing: 1px; white-space: nowrap; }
  .experience-note {
    margin-top: 8px; width: 352px; padding: 4px 14px 6px;
    background: var(--brand-blue); color: #fff;
    font-size: 22px; font-weight: 500; line-height: 1.2;
  }

  .worker-photo {
    position: absolute; left: 420px; top: 790px; width: 596px; height: 410px;
    background: linear-gradient(160deg, rgba(244,245,247,0) 0%, #6d7890 40%, #3a4257 75%, #2c2f36 100%);
    clip-path: polygon(60% 0, 100% 0, 100% 100%, 0 100%, 12% 70%, 45% 40%);
  }

  .seal { position: absolute; left: 532px; top: 842px; width: 224px; height: 224px; }
  .seal-text {
    position: absolute; left: 514px; top: 904px; width: 260px;
    transform: rotate(-22deg); text-align: center; white-space: nowrap;
    font-family: 'Oswald', sans-serif; color: #fff; line-height: 1.05;
    text-shadow: 0 1px 2px rgba(0,0,0,0.35);
  }
  .seal-text .small { font-size: 20px; font-weight: 500; display: block; }
  .seal-text .big { font-size: 31px; font-weight: 600; display: block; }
  .seal-text .tiny { font-size: 17px; font-weight: 600; display: block; font-family: 'Poppins', sans-serif; }

  .footer {
    position: absolute; left: 0; top: 1200px; width: 1016px; height: 116px;
    background: var(--footer-black); color: #fff;
  }
  .footer-plant {
    position: absolute; left: 166px; top: 30px; white-space: nowrap;
    color: var(--brand-blue); font-weight: 600; font-size: 26px; letter-spacing: 0.5px;
  }
  .footer-address {
    position: absolute; left: 444px; top: 22px; white-space: nowrap;
    font-size: 20px; font-weight: 500; line-height: 1.25; padding-left: 22px;
  }
  .footer-address svg { position: absolute; left: 0; top: 4px; }
  .footer-call { position: absolute; left: 786px; top: 22px; font-size: 20px; line-height: 1.2; white-space: nowrap; }
  .footer-call .call-label { color: var(--brand-blue); font-weight: 600; font-size: 21px; display: block; }
  .footer-call .call-number { font-weight: 600; font-size: 22px; display: block; }
  .footer-call svg { vertical-align: -2px; margin-right: 6px; }
</style>
</head>
<body>
<main class="flyer">
  <section class="brand-panel">
    <div class="brand-mark"></div>
    <div class="brand-name">HAWKFORGE<span>STRUCTURAL</span></div>
  </section>

  <div class="stock-photo" role="img" aria-label="Grid of steel stock: round bars, angle iron, square tubes and beams"></div>
  <div class="tube-photo" role="img" aria-label="Stack of square steel tubes"></div>

  <h1 class="headline">
    <div class="headline-top"><b>HAWK</b><i>FORGE</i></div>
    <div class="headline-bottom">METAL FABRICATOR</div>
  </h1>

  <section class="features">
    <div class="rule" style="left:254px; top:5px; width:2px; height:175px;"></div>
    <div class="rule" style="left:254px; top:230px; width:2px; height:170px;"></div>
    <div class="rule" style="left:48px; top:216px; width:178px; height:2px;"></div>
    <div class="rule" style="left:279px; top:216px; width:180px; height:2px;"></div>

    <div class="feature" style="left:27px; top:30px;">
      <div class="feature-icon">
        <svg width="52" height="52" viewBox="0 0 52 52" fill="none" stroke="#45669c" stroke-width="3" stroke-linejoin="round">
          <path d="M6 34 L26 22 L46 34 L26 46 Z"/><path d="M6 34 V40 L26 52"/><path d="M16 18 L38 6 M22 22 L44 10"/>
        </svg>
      </div>
      <div class="feature-label">Laser<br>Accuracy</div>
    </div>
    <div class="feature" style="left:259px; top:30px;">
      <div class="feature-icon">
        <svg width="52" height="52" viewBox="0 0 52 52" fill="none" stroke="#45669c" stroke-width="3" stroke-linecap="round">
          <circle cx="22" cy="22" r="15"/><path d="M22 13 V22 L28 26"/>
          <rect x="28" y="30" width="18" height="16" rx="2"/><path d="M32 38 L36 42 L42 34"/>
        </svg>
      </div>
      <div class="feature-label">On-Time<br>Scheduling</div>
    </div>
    <div class="feature" style="left:27px; top:230px;">
      <div class="feature-icon">
        <svg width="52" height="52" viewBox="0 0 52 52" fill="none" stroke="#45669c" stroke-width="3" stroke-linecap="round" stroke-linejoin="round">
          <path d="M36 8 A10 10 0 0 0 30 24 L10 44 L14 48 L34 28 A10 10 0 0 0 48 16 L42 22 L36 20 L34 14 Z"/>
        </svg>
      </div>
      <div class="feature-label">Own Our<br>Equipment</div>
    </div>
    <div class="feature" style="left:254px; top:230px;">
      <div class="feature-icon">
        <svg width="52" height="52" viewBox="0 0 52 52" fill="none" stroke="#45669c" stroke-width="3" stroke-linecap="round">
          <rect x="6" y="8" width="40" height="30" rx="2"/><path d="M12 16 H34 M12 22 H28 M12 28 H24"/>
          <circle cx="36" cy="32" r="6"/><path d="M32 37 L30 46 L36 42 L42 46 L40 37"/>
        </svg>
      </div>
      <div class="feature-label">Certified<br>Welders</div>
    </div>
  </section>

  <section class="experience">
    <div class="experience-years">39 YEARS</div>
    <div class="experience-word">EXPERIENCE</div>
    <div class="experience-note">Manufacturing Construction Brackets SINCE 1982</div>
  </section>

  <div class="worker-photo" role="img" aria-label="Worker in hard hat grinding steel at a vise"></div>

  <svg class="seal" viewBox="0 0 224 224" aria-hidden="true">
    <defs>
      <linearGradient id="sealFill" x1="0" y1="0" x2="1" y2="1">
        <stop offset="0" stop-color="#c9ccd1"/><stop offset="0.5" stop-color="#8e939b"/><stop offset="1" stop-color="#b4b8be"/>
      </linearGradient>
    </defs>
    <polygon fill="url(#sealFill)" points="112,4 124,26 143,9 149,33 172,22 171,47 196,42 188,66 213,68 198,88 220,100 200,114 218,131 194,138 206,160 181,161 185,186 161,180 158,205 136,193 124,216 112,196 100,216 88,193 66,205 63,180 39,186 43,161 18,160 30,138 6,131 24,114 4,100 26,88 11,68 36,66 28,42 53,47 52,22 75,33 81,9 100,26"/>
  </svg>
  <div class="seal-text">
    <span class="small">WE MANUFACTURE</span>
    <span class="big">CUSTOM IBEAMS</span>
    <span class="tiny">IN PHOENIX, AZ</span>
  </div>

  <footer class="footer">
    <div class="footer-plant">HAWKFORGE PLANT</div>
    <div class="footer-address">
      <svg width="14" height="18" viewBox="0 0 14 18"><path d="M7 0 A7 7 0 0 1 14 7 C14 12 7 18 7 18 C7 18 0 12 0 7 A7 7 0 0 1 7 0 Z" fill="#45669c"/><circle cx="7" cy="7" r="2.6" fill="#232323"/></svg>
      2814 n. 17th avenue, suite-3<br>Phx, AZ 85019
    </div>
    <div class="footer-call">
      <span class="call-label">CALL TODAY!</span>
      <span class="call-number"><svg width="18" height="18" viewBox="0 0 24 24"><path fill="#45669c" d="M6.6 10.8a15.1 15.1 0 0 0 6.6 6.6l2.2-2.2a1 1 0 0 1 1-.25 11.4 11.4 0 0 0 3.6.57 1 1 0 0 1 1 1V20a1 1 0 0 1-1 1A17 17 0 0 1 3 4a1 1 0 0 1 1-1h3.5a1 1 0 0 1 1 1c0 1.25.2 2.450.57 3.57a1 1 0 0 1-.25 1z"/></svg>480-629-8107</span>
    </div>
  </footer>
</main>
</body>
</html>
```